Corvane Supplies Business Card

Professional business card that stand out to our potential customers. Front and back with clean modern design

Industry/Entity Type

Oil and gas

Contact Information for Business Card

Name, address, website , office phone and cell number

Requirements
Must have
• Editable files for each employee

```html
<!DOCTYPE html>
<html lang="en">
<head>
<meta charset="utf-8">
<title>Corvane Supplies Business Card</title>
<link rel="stylesheet" href="https://fonts.googleapis.com/css2?family=Montserrat:wght@400;700;800&display=swap">
<style>
  :root {
    --red: #ec2029;
    --blue: #0fb0d4;
    --white: #ffffff;
    --stage: #e9e6e1;
    --shadow: rgba(40, 30, 20, 0.25);
  }
  * { margin: 0; padding: 0; box-sizing: border-box; }
  html, body { width: 1200px; height: 1014px; overflow: hidden; }
  body {
    background: var(--stage);
    font-family: "Montserrat", sans-serif;
    position: relative;
  }
  .card {
    position: absolute;
    width: 560px;
    height: 320px;
    border-radius: 3px;
    box-shadow: 0 10px 24px var(--shadow);
    overflow: hidden;
  }
  .card--back { left: 70px; top: 110px; display: flex; }
  .card--front {
    left: 570px; top: 580px;
    background: var(--white);
    display: flex; align-items: center; justify-content: center;
  }
  .brand-panel {
    width: 38%;
    background: var(--red);
    display: flex; align-items: center; justify-content: center;
    gap: 10px;
    border-right: 3px solid var(--white);
  }
  .brand-name {
    font-weight: 800;
    text-transform: uppercase;
    letter-spacing: 0.04em;
    line-height: 1.1;
  }
  .brand-panel .brand-name { color: var(--white); font-size: 22px; }
  .brand-square { width: 14px; height: 14px; background: var(--white); flex: none; }
  .contact-panel {
    flex: 1;
    background: var(--blue);
    color: var(--white);
    padding: 44px 30px 0 34px;
  }
  .person-name { font-weight: 700; font-size: 22px; }
  .person-title { font-weight: 400; font-size: 16px; margin-bottom: 22px; }
  .contact-list { list-style: none; font-size: 14px; line-height: 1.65; }
  .contact-list li { display: flex; align-items: flex-start; gap: 8px; }
  .contact-list svg { width: 13px; height: 13px; margin-top: 5px; flex: none; }
  .card--front .brand-name { color: var(--red); font-size: 34px; }
  .card--front .brand-square { background: var(--blue); width: 22px; height: 22px; margin-right: 14px; }
</style>
</head>
<body>
  <section class="card card--back" aria-label="Card back">
    <div class="brand-panel">
      <span class="brand-square"></span>
      <span class="brand-name">Corvane<br>Supplies</span>
    </div>
    <div class="contact-panel">
      <p class="person-name">Dale Hartwell</p>
      <p class="person-title">Manager &amp; Owner</p>
      <ul class="contact-list">
        <li><svg viewBox="0 0 16 16" fill="none" stroke="currentColor" stroke-width="1.5"><path d="M3 1.5l3 3-1.5 2c1 2 3 4 5 5l2-1.5 3 3-2 2C7 14 2 9 1.5 3.5z"/></svg>(832) 555-0147</li>
        <li><svg viewBox="0 0 16 16" fill="none" stroke="currentColor" stroke-width="1.5"><rect x="4" y="1" width="8" height="14" rx="1"/><line x1="7" y1="12.5" x2="9" y2="12.5"/></svg>(604) 555-0192</li>
        <li><svg viewBox="0 0 16 16" fill="none" stroke="currentColor" stroke-width="1.5"><rect x="1" y="3" width="14" height="10"/><path d="M1 3l7 6 7-6"/></svg>sales@corvanesupplies.com</li>
        <li><svg viewBox="0 0 16 16" fill="none" stroke="currentColor" stroke-width="1.3"><circle cx="8" cy="8" r="6.5"/><ellipse cx="8" cy="8" rx="3" ry="6.5"/><line x1="1.5" y1="8" x2="14.5" y2="8"/></svg>corvanesupplies.com</li>
        <li><svg viewBox="0 0 16 16" fill="none" stroke="currentColor" stroke-width="1.5"><path d="M1.5 8L8 2l6.5 6M3.5 6.5V14h9V6.5"/><rect x="6.5" y="10" width="3" height="4"/></svg><span>420 N.Larkspur Suite 5<br>Kestrel, Tx 79711</span></li>
      </ul>
    </div>
  </section>

  <section class="card card--front" aria-label="Card front">
    <span class="brand-square"></span>
    <span class="brand-name">Corvane Supplies</span>
  </section>
</body>
</html>
```